Tarvell homes and renovations business card design.

Would like some new card designs utilizing my new logo that look professional. I am open to different colors on the logo or utilize the same ones we have. I like the original concept but would like to see some fresh ideas and build on what we have already done.

Target Market(s)

Custom home building industry, Real estate sales, Renovation projects.

Industry/Entity Type

Home Builder

Contact Information for Business Card

Tarvell Homes and Renovations
2871 162nd Street
Frank, Alberta
T0L3P0
Home : 403- 555-0187 Cell: 403- 555-0243

My info is : Gus Tarvell, President and CEO
email: tarvellhomes@quillmail.example
Website: tarvellhomes.example

Requirements
Must have
• Must Use my new logo design. I am open to different colors on the logo or utilize the same ones in the existing design. I can upload the original logo design if needed.

```html
<!DOCTYPE html>
<html lang="en">
<head>
<meta charset="utf-8">
<title>Tarvell Homes and Renovations – Business Card</title>
<link href="https://fonts.googleapis.com/css2?family=Open+Sans:wght@400;600;700&display=swap" rel="stylesheet">
<style>
  :root {
    --backdrop: #e9e6e1;
    --card-white: #ffffff;
    --card-black: #1b1b1b;
    --gold: #b98a2e;
    --gold-light: #c9a04a;
    --text-grey: #6b6b6b;
    --silver: #a9a9a9;
  }
  * { margin: 0; padding: 0; box-sizing: border-box; }
  html, body {
    width: 1200px; height: 1000px; overflow: hidden;
    background: var(--backdrop);
    font-family: "Open Sans", Arial, sans-serif;
  }
  .canvas { position: relative; width: 1200px; height: 1000px; }
  .card {
    position: absolute; left: 266px; width: 666px; height: 397px;
    overflow: hidden; box-shadow: 0 4px 14px rgba(0,0,0,0.18);
  }
  .card--front { top: 74px; background: var(--card-white); }
  .card--back { top: 534px; background: var(--card-black); }

  .contact { position: absolute; left: 32px; top: 68px; color: var(--text-grey); font-size: 16px; }
  .contact__name { color: var(--gold); font-weight: 700; font-size: 21px; letter-spacing: 0.3px; line-height: 28px; }
  .contact__title { line-height: 22px; }
  .contact__address { margin-top: 20px; line-height: 24px; }
  .contact__list { list-style: none; margin-top: 11px; }
  .contact__item { display: flex; align-items: center; gap: 7px; line-height: 24.6px; }
  .contact__icon { width: 13px; height: 13px; fill: var(--gold); flex: none; }

  .brand { position: absolute; text-align: center; font-weight: 600; }
  .brand--front { right: 32px; top: 222px; width: 300px; color: var(--gold); }
  .brand--back { left: 0; right: 0; top: 225px; color: var(--silver); }
  .brand__name { display: block; font-size: 50px; line-height: 52px; letter-spacing: 1px; }
  .brand__tagline { display: block; font-size: 18px; line-height: 22px; letter-spacing: 0.5px; }
  .brand--back .brand__name { font-size: 60px; line-height: 62px; }
  .brand--back .brand__tagline { font-size: 21px; }
  .brand__mark { display: inline-block; width: 14px; height: 14px; margin-bottom: 14px; }
  .brand--front .brand__mark { background: var(--gold); }
  .brand--back .brand__mark { background: var(--silver); }

  .wave { position: absolute; left: 0; bottom: 0; width: 666px; height: 90px; }
</style>
</head>
<body>
<main class="canvas">
  <section class="card card--front">
    <div class="contact">
      <p class="contact__name">GUS TARVELL</p>
      <p class="contact__title">President / CEO</p>
      <p class="contact__address">2871 162nd Street<br>Frank, Alberta T0L3P0</p>
      <ul class="contact__list">
        <li class="contact__item"><svg class="contact__icon" viewBox="0 0 13 13"><path d="M3.5 0h6a1 1 0 0 1 1 1v11a1 1 0 0 1-1 1h-6a1 1 0 0 1-1-1V1a1 1 0 0 1 1-1zm.5 1.5v9h5v-9z"/></svg>403- 555-0243</li>
        <li class="contact__item"><svg class="contact__icon" viewBox="0 0 13 13"><path d="M1 4c0-2 3-3 5.5-3S12 2 12 4v1H9V3.8H4V5H1zM2 6h9l1 6H1z"/></svg>403- 555-0187</li>
        <li class="contact__item"><svg class="contact__icon" viewBox="0 0 13 13"><path d="M0 2.5h13v8H0zm1 1 5.5 4 5.5-4z"/></svg>tarvellhomes@quillmail.example</li>
        <li class="contact__item"><svg class="contact__icon" viewBox="0 0 13 13"><circle cx="6.5" cy="6.5" r="6"/></svg>www.tarvellhomes.example</li>
      </ul>
    </div>
    <div class="brand brand--front">
      <span class="brand__mark"></span>
      <span class="brand__name">TARVELL</span>
      <span class="brand__tagline">HOMES AND RENOVATIONS</span>
    </div>
    <svg class="wave" viewBox="0 0 666 90" preserveAspectRatio="none">
      <path d="M0 40 C120 -10 300 20 420 45 C520 65 600 60 666 30 V90 H0Z" fill="var(--card-black)"/>
      <path d="M0 40 C120 -10 300 20 420 45 C520 65 600 60 666 30 V36 C600 66 520 72 420 52 C300 28 120 -2 0 46Z" fill="#ffffff"/>
      <path d="M90 6 C220 -6 330 18 440 36 C540 52 600 40 640 22 C600 48 530 58 430 44 C320 28 220 6 90 6Z" fill="var(--gold)"/>
    </svg>
  </section>

  <section class="card card--back">
    <div class="brand brand--back">
      <span class="brand__mark"></span>
      <span class="brand__name">TARVELL</span>
      <span class="brand__tagline">HOMES AND RENOVATIONS</span>
    </div>
  </section>
</main>
</body>
</html>
```